Website design for Tallow Ridge Trading Inc

We are looking to build a website for our company. We are a scrap metal recycling company based out of Los Angeles. We purchase scrap metal in the US and ship them to China for recycling into fresh metal ores to supply industrial users. We would designs that emphasize the color green given our name and the nature of our business. Recycling themes are welcomed. We already have a URL at:
http://tallowridgetradinginc.example/
At this point, I would like 4 pages:
- Home page
- About Us
- Resources
- Contact us
Our sister company is Marrow Peak Intl Inc and they have a website that we can use as a starting point.
http://www.marrowpeak-intl.example/
Our competitor has a website below. However we dislike the design given we believe it looks rather dull.
http://www.vesperalloyworks.example/en/
Lastly, this is for a website shell only. Please design the template, graphics, and color schemes. We will write the contents later.

```html
<!DOCTYPE html>
<html lang="en">
<head>
<meta charset="utf-8">
<title>Tallow Ridge Trading Inc</title>
<link rel="stylesheet" href="https://fonts.googleapis.com/css2?family=Jost:wght@400;500&family=Arimo:wght@400&display=swap">
<style>
  :root {
    --page-top: #66777a;
    --page-bottom: #5b6a6b;
    --teal: #2a8a84;
    --gold: #efba2e;
    --ink: #111;
    --white: #fff;
    --slate: #3b4a4a;
    --grey-text: #7d8a8a;
    --band: rgba(28, 36, 34, 0.86);
    --footer: #5b6a68;
    --body-text: #222;
  }
  * { box-sizing: border-box; margin: 0; padding: 0; }
  html, body { width: 1200px; height: 1016px; overflow: hidden; }
  body {
    background: linear-gradient(var(--page-top) 0 718px, var(--page-bottom) 718px 100%);
    font-family: "Arimo", Arial, sans-serif;
    position: relative;
  }
  .site { position: absolute; left: 88px; top: 0; width: 1026px; height: 1016px; }

  .brand {
    position: absolute; left: 0; top: 0; width: 330px; height: 139px;
    background: var(--teal); color: var(--white);
    font-family: "Jost", sans-serif; font-weight: 400;
    text-align: right; padding: 22px 28px 0 0;
  }
  .brand-line1 { font-size: 41px; line-height: 48px; display: block; }
  .brand-line2 { font-size: 29px; line-height: 34px; display: block; letter-spacing: 1px; text-transform: uppercase; }

  .social { position: absolute; right: 24px; top: 17px; display: flex; gap: 10px; }
  .social span { width: 23px; height: 23px; border-radius: 4px; background: var(--teal); }
  .social span + span { background: #8fcfcf; }

  .nav {
    position: absolute; left: 330px; top: 57px; width: 696px; height: 82px;
    background: var(--gold);
    display: flex; justify-content: flex-end; align-items: center; gap: 39px;
    padding-right: 49px;
  }
  .nav a {
    font-family: "Jost", sans-serif; font-size: 17px; color: var(--ink);
    text-decoration: none; text-transform: uppercase;
  }

  .hero { position: absolute; left: 0; top: 139px; width: 1026px; height: 576px; }
  .hero-photo {
    position: absolute; inset: 0;
    background: linear-gradient(170deg, #3e4846 0%, #6f7c76 30%, #5f6c66 55%, #2d8f86 70%, #56625e 85%, #4c5652 100%);
  }
  .welcome {
    position: absolute; left: 0; top: 0; width: 100%; height: 127px;
    background: var(--band); padding: 10px 40px 0 47px;
  }
  .welcome h1 {
    font-family: "Jost", sans-serif; font-weight: 400; font-size: 33px;
    color: var(--gold); line-height: 40px;
  }
  .welcome p { color: #eef; font-size: 13px; line-height: 18px; margin-top: 2px; }

  .intro {
    position: absolute; left: 0; top: 715px; width: 1026px; height: 244px;
    background: var(--white);
  }
  .flow {
    position: absolute; left: 33px; top: 62px;
    display: flex; align-items: flex-start; gap: 20px;
    font-family: "Jost", sans-serif; color: var(--grey-text);
  }
  .flow-step { display: flex; flex-direction: column; align-items: flex-end; }
  .flow-step strong { font-weight: 500; font-size: 28px; line-height: 30px; }
  .flow-step small { font-size: 14px; line-height: 14px; }
  .flow svg { margin-top: 2px; }

  .about { position: absolute; left: 564px; top: 16px; width: 410px; }
  .about h2 {
    font-family: "Jost", sans-serif; font-weight: 500; font-size: 24px;
    color: var(--slate); line-height: 32px; margin-bottom: 6px;
  }
  .about p { font-size: 14px; line-height: 22.5px; color: var(--body-text); }

  .footer {
    position: absolute; left: 0; top: 959px; width: 1026px; height: 57px;
    background: var(--footer); color: var(--white);
    font-size: 11px; text-align: center; padding-top: 15px;
  }
</style>
</head>
<body>
<div class="site">
  <header>
    <div class="brand">
      <span class="brand-line1">Tallow Ridge</span>
      <span class="brand-line2">Trading Inc.</span>
    </div>
    <div class="social" aria-label="Social links"><span></span><span></span></div>
    <nav class="nav">
      <a href="#">Home</a>
      <a href="#">About Us</a>
      <a href="#">Resources</a>
      <a href="#">Contact Us</a>
    </nav>
  </header>

  <section class="hero">
    <div class="hero-photo" role="img" aria-label="Aerial photo of a teal container ship loaded with cargo containers sailing on grey-green water"></div>
    <div class="welcome">
      <h1>Welcome</h1>
      <p>Lorem ipsum dolor sit amet, consectetuer adipiscing elit. Nam cursus. Morbi ut mi. Nullam enim leo, egestas id, condimentum at, laoreet mattis, massa. Sed eleifend nonummy diam. Praesent mauris ante, elementum et, bibendum at, posuere sit amet, nibh. Duis tincidunt lectus quis dui viverra vestibulum. Suspendisse vulputate aliquam dui. Nulla elementum dui ut augue. Aliquam vehicula mi at mauris.</p>
    </div>
  </section>

  <section class="intro">
    <div class="flow">
      <div class="flow-step"><strong>Scrap Metal</strong><small>from USA</small></div>
      <svg width="44" height="48" viewBox="0 0 44 48" aria-hidden="true">
        <polygon points="0,0 20,0 44,24 20,48 0,48 24,24" fill="#7d8a8a"/>
      </svg>
      <div class="flow-step"><strong>Fresh Metal Ores</strong><small>to China</small></div>
    </div>
    <div class="about">
      <h2>About Us</h2>
      <p>Pellentesque habitant morbi tristique senectus et netus et malesuada fames ac turpis egestas. In posuere felis nec tortor. Pellentesque faucibus. Ut accumsan ultricies elit. Maecenas at justo id velit placerat molestie. Donec dictum lectus non odio. Cras a ante vitae enim iaculis aliquam. Mauris nunc quam, venenatis nec, euismod sit amet, egestas placerat, est. Pellentesque congue leo.</p>
    </div>
  </section>

  <footer class="footer">© 2013 Tallow Ridge Trading Inc. All Rights Reserved</footer>
</div>
</body>
</html>
```